Stationary (letterhead, envelopes, business cards and e-mail signature) for law firm
Law Office of Warren T. Felding
Creative Brief
Professional
Warren T. Felding
Attorney at Law
41 Linden Court, Suite 500 Irvine, California 92731
wfelding@lawwtf-example.com
www.lawwtf-example.com
I would also like my direct dial phone number to appear on the card (in addition to my main number. The Direct number is (714) 555-0187
I would like my logo and maybe my website address to appear on the back. Please be creative.

```html
<!DOCTYPE html>
<html lang="en">
<head>
<meta charset="utf-8">
<title>Law Office of Warren T. Felding – Business Card</title>
<link rel="stylesheet" href="https://fonts.googleapis.com/css2?family=Cinzel:wght@400;600&display=swap">
<style>
  :root {
    --navy: #1f2750;
    --grey: #9a9ca3;
    --paper: #ffffff;
    --backdrop: #e9e7e3;
    --ink-light: #f2f2f4;
  }
  html, body {
    margin: 0;
    width: 1200px;
    height: 914px;
    overflow: hidden;
    background: var(--backdrop);
  }
  .card {
    position: absolute;
    left: 100px;
    top: 171px;
    width: 1000px;
    height: 572px;
    background: var(--paper);
    box-shadow: 0 10px 30px rgba(0,0,0,0.18);
    font-family: "Cinzel", "Times New Roman", serif;
    overflow: hidden;
  }
  .card-shapes {
    position: absolute;
    inset: 0;
  }
  .holder {
    position: absolute;
    left: 72px;
    top: 52px;
    color: var(--ink-light);
  }
  .holder-name {
    margin: 0;
    font-size: 27px;
    font-weight: 600;
    letter-spacing: 0.5px;
  }
  .holder-title {
    margin: 6px 0 0;
    font-size: 17px;
    font-weight: 400;
    letter-spacing: 1px;
  }
  .contacts {
    position: absolute;
    left: 60px;
    top: 298px;
    margin: 0;
    padding: 0;
    list-style: none;
    color: var(--ink-light);
    font-size: 15.5px;
    line-height: 27px;
  }
  .contacts li {
    display: flex;
    align-items: center;
  }
  .contacts .icon {
    width: 17px;
    height: 17px;
    margin-right: 12px;
    flex: none;
  }
  .contacts .indent {
    padding-left: 29px;
  }
  .firm-mark {
    position: absolute;
    left: 640px;
    top: 248px;
    display: flex;
    align-items: center;
    color: var(--navy);
  }
  .firm-mark .square {
    width: 22px;
    height: 22px;
    background: var(--navy);
    margin-right: 18px;
    flex: none;
  }
  .firm-name {
    margin: 0;
    font-size: 25px;
    font-weight: 400;
    line-height: 34px;
    letter-spacing: 1.5px;
  }
</style>
</head>
<body>
  <div class="card">
    <svg class="card-shapes" viewBox="0 0 1000 572" width="1000" height="572" aria-hidden="true">
      <path d="M0 0 H560 Q560 330 410 572 H0 Z" fill="var(--navy)"/>
      <path d="M585 0 Q585 340 436 572" fill="none" stroke="var(--grey)" stroke-width="16"/>
    </svg>

    <div class="holder">
      <h1 class="holder-name">Warren T. Felding</h1>
      <p class="holder-title">Attorney at Law</p>
    </div>

    <ul class="contacts">
      <li>
        <svg class="icon" viewBox="0 0 20 20"><circle cx="10" cy="10" r="10" fill="#fff"/><path d="M10 4a4 4 0 0 0-4 4c0 3 4 8 4 8s4-5 4-8a4 4 0 0 0-4-4z" fill="var(--navy)"/><circle cx="10" cy="8" r="1.5" fill="#fff"/></svg>
        41 Linden Court, Suite 500
      </li>
      <li class="indent">Irvine, California 92731</li>
      <li>
        <svg class="icon" viewBox="0 0 20 20"><circle cx="10" cy="10" r="10" fill="#fff"/><path d="M7 5l2 3-1.2 1.2a7 7 0 0 0 3 3L12 11l3 2-1 2c-4 0-8-4-8-8z" fill="var(--navy)"/></svg>
        (714) 555-0142
      </li>
      <li>
        <svg class="icon" viewBox="0 0 20 20"><circle cx="10" cy="10" r="10" fill="#fff"/><rect x="7" y="4" width="6" height="12" rx="1" fill="var(--navy)"/></svg>
        (714) 555-0187
      </li>
      <li>
        <svg class="icon" viewBox="0 0 20 20"><circle cx="10" cy="10" r="10" fill="#fff"/><rect x="5" y="8" width="10" height="7" fill="var(--navy)"/><rect x="7" y="4" width="6" height="4" fill="var(--navy)"/></svg>
        (714) 555-0163
      </li>
      <li>
        <svg class="icon" viewBox="0 0 20 20"><circle cx="10" cy="10" r="10" fill="#fff"/><rect x="4.5" y="6" width="11" height="8" fill="var(--navy)"/><path d="M4.5 6l5.5 4.5L15.5 6" fill="none" stroke="#fff" stroke-width="1"/></svg>
        wfelding@lawwtf-example.com
      </li>
      <li>
        <svg class="icon" viewBox="0 0 20 20"><circle cx="10" cy="10" r="10" fill="#fff"/><circle cx="10" cy="10" r="5.5" fill="none" stroke="var(--navy)" stroke-width="1.5"/><path d="M4.5 10h11M10 4.5v11" stroke="var(--navy)" stroke-width="1.2"/></svg>
        www.lawwtf-example.com
      </li>
    </ul>

    <div class="firm-mark">
      <span class="square"></span>
      <p class="firm-name">Law Office of<br>Warren T. Felding</p>
    </div>
  </div>
</body>
</html>
```